Postcard: Open Sky Circle

Text for front: HOW TO CHANGE THE WORLD IN ONE [note: the word "one" should be underlined] STEPHint: It's up to you...[Note: add arrow or something to indicate "turn over"]Text for back: You're going to spend your entire life with someone you can never get away from. (Guess who?) Wouldn't you rather that person #OpenSkyCircle than judgmental or critical? BE the change you want to see! Visit www.OpenSkyCircle-hub.example for daily Dawn Pebbles and community. PLEASE JOIN US![Note: add logo to left half of back side]Font preference for text: Josefin sans

Target Market(s)

People who would be attracted to Corvane church - teravian perennist message. It's spiritual without being overtly religious, so the target market is probably early 30s and up but ideally won't turn off Millennials (folks under 30). It should attract attention of people who are open-minded and committed to progressive social change, tired of an atmosphere of hate-mongering and divisiveness.

Requirements
Nice to have
• It would be nice to convey a sense of challenge - there is an idea of "dawn pebbles" so something related to fire/sparks is appropriate. This is meant to evoke a deeper, divine love more than a sense of romantic love. This love is more fierce than fluffy! Yet it calls us to be our best selves.
Should not have
• Please avoid excessive pink - just the logo is enough, as this design needs to appeal to men as well as women.

```html
<!DOCTYPE html>
<html lang="en">
<head>
<meta charset="utf-8">
<title>Open Sky Circle Postcard</title>
<link rel="stylesheet" href="https://fonts.googleapis.com/css2?family=Josefin+Sans:wght@300;400;600;700&display=swap">
<style>
  :root {
    --backdrop: #8c8c8c;
    --backdrop-light: #a3a3a3;
    --pink: #ee6f9e;
    --pink-light: #f48cb3;
    --pink-deep: #e4578a;
    --white: #ffffff;
    --pill: #e6e6e6;
    --ink: #5a5a5a;
    --fold: #f2f2f2;
  }
  * { box-sizing: border-box; margin: 0; padding: 0; }
  html, body { width: 900px; height: 1200px; overflow: hidden; }
  body {
    font-family: "Josefin Sans", sans-serif;
    background: radial-gradient(circle at 50% 45%, var(--backdrop-light), var(--backdrop) 75%);
    position: relative;
  }
  .postcard {
    position: absolute;
    left: 60px;
    width: 780px;
    height: 535px;
    box-shadow: 0 6px 18px rgba(0,0,0,0.3);
    overflow: hidden;
  }

  /* Front */
  .postcard--front {
    top: 45px;
    background: linear-gradient(135deg, var(--pink-light), var(--pink) 55%, var(--pink-deep));
    color: var(--white);
  }
  .front-title {
    position: absolute;
    top: 70px;
    left: 0;
    width: 100%;
    text-align: center;
    text-transform: uppercase;
    font-weight: 300;
  }
  .front-title__lead {
    display: block;
    font-size: 52px;
    line-height: 1.1;
    letter-spacing: 1px;
  }
  .front-title__punch {
    display: block;
    margin-top: 14px;
    font-size: 96px;
    line-height: 1;
  }
  .front-title__one {
    font-weight: 700;
    text-decoration: underline;
    text-decoration-thickness: 6px;
    text-underline-offset: 10px;
  }
  .hint-pill {
    position: absolute;
    top: 382px;
    left: 120px;
    width: 420px;
    height: 72px;
    border-radius: 36px;
    background: var(--pill);
    color: var(--ink);
    font-size: 36px;
    font-weight: 400;
    display: flex;
    align-items: center;
    padding-left: 34px;
    padding-top: 6px;
  }
  .turn-corner {
    position: absolute;
    top: 0;
    right: 0;
    width: 120px;
    height: 120px;
  }

  /* Back */
  .postcard--back {
    top: 620px;
    background: var(--white);
  }
  .brand-mark {
    position: absolute;
    left: 70px;
    top: 60px;
    width: 250px;
    height: 250px;
    display: flex;
    flex-direction: column;
    align-items: center;
    justify-content: center;
    gap: 18px;
  }
  .brand-mark__dot {
    width: 110px;
    height: 110px;
    border-radius: 50%;
    background: var(--pink);
  }
  .brand-mark__name {
    font-size: 30px;
    font-weight: 400;
    color: var(--pink);
    text-align: center;
    line-height: 1.1;
  }
  .back-message {
    position: absolute;
    left: 375px;
    top: 45px;
    width: 370px;
    font-size: 19px;
    line-height: 1.3;
    color: var(--ink);
    font-weight: 400;
  }
  .back-message__you {
    color: var(--pink);
    font-size: 38px;
    font-weight: 400;
  }
  .visit-band {
    position: absolute;
    left: 375px;
    right: 0;
    top: 243px;
    height: 80px;
    background: var(--pink);
    color: var(--white);
    font-size: 19px;
    line-height: 1.3;
    text-align: center;
    display: flex;
    align-items: center;
    justify-content: center;
    padding: 6px 20px 0;
  }
  .join-band {
    position: absolute;
    left: 0;
    right: 0;
    top: 395px;
    height: 125px;
    background: var(--pink);
    border-top: 6px solid var(--pink-light);
    color: var(--white);
    font-size: 78px;
    font-weight: 300;
    text-transform: uppercase;
    letter-spacing: 2px;
    display: flex;
    align-items: center;
    justify-content: center;
    padding-top: 10px;
  }
</style>
</head>
<body>
  <section class="postcard postcard--front" aria-label="Postcard front">
    <h1 class="front-title">
      <span class="front-title__lead">How to change</span>
      <span class="front-title__lead">the world</span>
      <span class="front-title__punch">In <span class="front-title__one">One</span> Step</span>
    </h1>
    <p class="hint-pill">Hint: It's up to you</p>
    <svg class="turn-corner" viewBox="0 0 120 120" aria-hidden="true">
      <polygon points="0,0 120,120 120,0" fill="#9a9a9a" opacity="0.55"/>
      <polygon points="0,0 120,120 40,80" fill="var(--fold)"/>
    </svg>
  </section>

  <section class="postcard postcard--back" aria-label="Postcard back">
    <div class="brand-mark">
      <span class="brand-mark__dot"></span>
      <span class="brand-mark__name">Open Sky Circle</span>
    </div>
    <p class="back-message">
      <span class="back-message__you">You</span> are going to spend your entire life with someone you can never get away from. (Guess who?) Wouldn't you rather that person #OpenSkyCircle than judgmental or critical? BE the change you want to see!
    </p>
    <p class="visit-band">Visit www.OpenSkyCircle-hub.example<br>for daily Dawn Pebbles and community.</p>
    <p class="join-band">Please join us!</p>
  </section>
</body>
</html>
```